Boom Way Hoist Service Business Cards

I need a business card for "Boom Way Hoist and Haulage"

Boomway2023@hoistmail.net

Hoist Works LLC, Boom Way Hoist and Haulage LLC

555.014.7260 | www.BOOMWAYHOISTS.example

Central Indiana & Northeast Ohio

(IN) 14820 Maple Lane Noblesville, IN 46000

(OH) 2450 Pell Street Akron, Ohio 44300

Colors
0094D4
00A9DD
6FCCEA
C7EBF8
E9F6FB
59FF00
82FF00
B8FF75
E3FFCB
F4FFEA
EE7325
F08F49
F5BC92
FAE3D3
FDF4ED
EB3D1F
EC4F4E
F09395
F8D3D4
FCEDEE
E54698
E96AAD
F1A4CE
F9D9EA
FCEFF6
A7469A
B969AE
D3A5CF
EDDBEB
F8F0F9

```html
<!DOCTYPE html>
<html lang="en">
<head>
<meta charset="utf-8">
<title>Boom Way Hoist and Haulage – Business Cards</title>
<link rel="stylesheet" href="https://fonts.googleapis.com/css2?family=Questrial&display=swap">
<style>
  :root {
    --bg: #e9e6e1;
    --card-white: #ffffff;
    --card-black: #060606;
    --ink: #1c1c1c;
    --paper-text: #ffffff;
    --accent-red: #eb3d1f;
    --accent-green: #59ff00;
    --steel: #8a8a8a;
  }
  * { box-sizing: border-box; margin: 0; padding: 0; }
  html, body { width: 1200px; height: 900px; overflow: hidden; }
  body {
    background: var(--bg);
    font-family: "Questrial", "Century Gothic", sans-serif;
    position: relative;
  }
  .card {
    position: absolute;
    left: 250px;
    width: 700px;
    height: 400px;
    overflow: hidden;
    box-shadow: 0 10px 28px rgba(0,0,0,0.18);
  }
  .card-front {
    top: 35px;
    background: var(--card-white);
    border-radius: 48px 0 48px 0;
  }
  .card-back {
    top: 465px;
    background: var(--card-black);
    border-radius: 0 48px 0 48px;
  }
  .front-url {
    position: absolute;
    top: 46px;
    right: 52px;
    font-size: 21px;
    letter-spacing: 4px;
    color: var(--ink);
  }
  .front-url .domain { color: var(--accent-red); }
  .front-scene {
    position: absolute;
    left: 70px;
    bottom: 42px;
    width: 250px;
    height: 200px;
    border-radius: 4px;
    background: linear-gradient(135deg, #d9d9d9 0%, #9c9c9c 45%, #e2583a 70%, #3fbf3f 100%);
  }
  .contact-list {
    position: absolute;
    left: 48px;
    top: 70px;
    list-style: none;
    color: var(--paper-text);
    font-size: 23px;
    line-height: 38px;
  }
  .contact-list li { display: flex; align-items: center; gap: 12px; }
  .contact-list .icon { width: 22px; height: 22px; flex: none; }
  .contact-list .indent { padding-left: 34px; }
  .region { color: var(--accent-red); }
  .state-tag { color: var(--accent-red); }
  .brand-lockup {
    position: absolute;
    right: 48px;
    bottom: 56px;
    display: flex;
    align-items: center;
    gap: 14px;
  }
  .brand-mark {
    width: 22px; height: 22px;
    background: var(--accent-green);
  }
  .brand-name {
    color: var(--paper-text);
    font-size: 30px;
    letter-spacing: 1px;
  }
</style>
</head>
<body>

<section class="card card-front">
  <p class="front-url">www.<span class="domain">BOOMWAYHOISTS</span>.example</p>
  <div class="front-scene" role="img" aria-label="Illustration of a red boom truck and a green mobile crane in front of steel building frames"></div>
</section>

<section class="card card-back">
  <ul class="contact-list">
    <li>
      <svg class="icon" viewBox="0 0 24 24" aria-hidden="true"><path fill="#eb3d1f" d="M6.6 10.8a15 15 0 0 0 6.6 6.6l2.2-2.2a1 1 0 0 1 1-.25 11.4 11.4 0 0 0 3.6.6 1 1 0 0 1 1 1V20a1 1 0 0 1-1 1A17 17 0 0 1 3 4a1 1 0 0 1 1-1h3.5a1 1 0 0 1 1 1c0 1.25.2 2.45.57 3.57a1 1 0 0 1-.25 1z"/></svg>
      555.014.7260
    </li>
    <li>
      <svg class="icon" viewBox="0 0 24 24" aria-hidden="true"><rect x="2" y="5" width="20" height="14" rx="2" fill="#eb3d1f"/><path d="M3 7l9 6 9-6" fill="none" stroke="#060606" stroke-width="1.8"/></svg>
      Boomway2023@hoistmail.net
    </li>
    <li>
      <svg class="icon" viewBox="0 0 24 24" aria-hidden="true"><circle cx="12" cy="12" r="9" fill="none" stroke="#eb3d1f" stroke-width="2"/><path d="M3 12h18M12 3c3 3 3 15 0 18M12 3c-3 3-3 15 0 18" fill="none" stroke="#eb3d1f" stroke-width="1.6"/></svg>
      www.BOOMWAYHOISTS.example
    </li>
    <li>
      <svg class="icon" viewBox="0 0 24 24" aria-hidden="true"><path fill="#eb3d1f" d="M12 2a7 7 0 0 0-7 7c0 5 7 13 7 13s7-8 7-13a7 7 0 0 0-7-7zm0 9.5A2.5 2.5 0 1 1 12 6.5a2.5 2.5 0 0 1 0 5z"/></svg>
      <span class="region">Central Indiana &amp; Northeast Ohio</span>
    </li>
    <li class="indent"><span class="state-tag">(IN)</span>&nbsp;14820 Maple Lane Noblesville, IN 46000</li>
    <li class="indent"><span class="state-tag">(OH)</span>&nbsp;2450 Pell Street Akron, Ohio 44300</li>
  </ul>

  <div class="brand-lockup">
    <span class="brand-mark" aria-hidden="true"></span>
    <span class="brand-name">Boom Way Hoist and Haulage</span>
  </div>
</section>

</body>
</html>
```